Need business card designed - Ive attached a document. On the top is a business card design that I like. Below that, hand written are the elements that I need to be on my card. I'm attaching photo and logo. thank you!

Industry/Entity Type

Business

```html
<!DOCTYPE html>
<html lang="en">
<head>
<meta charset="utf-8">
<title>Harwell Mortgage Advisors – Business Card</title>
<link rel="stylesheet" href="https://fonts.googleapis.com/css2?family=Arimo:wght@400;700&display=swap">
<style>
  :root {
    --page: #ffffff;
    --navy: #0c2572;
    --navy-text: #132a7a;
    --silver-light: #f4f4f5;
    --silver-mid: #d9dadc;
    --silver-dark: #b9babd;
    --white: #ffffff;
    --photo-top: #4f7a45;
    --photo-bottom: #8fd3d6;
  }
  * { margin: 0; padding: 0; box-sizing: border-box; }
  html, body {
    width: 1200px;
    height: 842px;
    overflow: hidden;
    background: var(--page);
    font-family: "Arimo", Arial, sans-serif;
  }
  .canvas {
    position: relative;
    width: 1200px;
    height: 842px;
  }
  .card {
    position: absolute;
    left: 137px;
    top: 169px;
    width: 891px;
    height: 516px;
    background: var(--navy);
    overflow: hidden;
  }
  .card__band {
    position: absolute;
    left: 0; top: 0;
    width: 100%;
    height: 219px;
    background: linear-gradient(90deg, var(--silver-dark) 0%, var(--silver-light) 30%, var(--silver-mid) 60%, var(--silver-light) 82%, var(--silver-dark) 100%);
  }
  .card__rule {
    position: absolute;
    left: 0; top: 219px;
    width: 100%;
    height: 12px;
    background: linear-gradient(90deg, var(--silver-dark) 0%, var(--white) 35%, var(--silver-mid) 65%, var(--white) 100%);
  }
  .portrait {
    position: absolute;
    left: 58px;
    top: 52px;
    width: 207px;
    height: 281px;
    background: linear-gradient(180deg, var(--photo-top) 0%, #9c8a6c 45%, var(--photo-bottom) 100%);
  }
  .brand {
    position: absolute;
    left: 426px;
    top: 48px;
    width: 221px;
    height: 84px;
    display: flex;
    align-items: center;
    justify-content: center;
    text-align: center;
    color: var(--navy-text);
    font-weight: 700;
    font-size: 22px;
    line-height: 1.15;
    letter-spacing: 1px;
  }
  .website {
    position: absolute;
    left: 365px;
    top: 176px;
    width: 400px;
    text-align: center;
    color: var(--navy-text);
    font-weight: 700;
    font-size: 26px;
  }
  .name {
    position: absolute;
    left: 300px;
    width: 500px;
    text-align: center;
    color: var(--white);
    font-weight: 700;
  }
  .name--first { top: 262px; font-size: 52px; letter-spacing: 7px; }
  .name--last  { top: 334px; font-size: 27px; letter-spacing: 4px; }
  .phone {
    position: absolute;
    left: 340px;
    top: 410px;
    display: flex;
    align-items: center;
    gap: 14px;
    color: var(--white);
    font-weight: 700;
    font-size: 27px;
  }
  .phone__icon { width: 22px; height: 32px; }
  .title {
    position: absolute;
    left: 32px;
    top: 348px;
    width: 260px;
    text-align: center;
    color: var(--white);
    font-size: 24px;
    line-height: 40px;
  }
  .title__role { font-weight: 700; }
</style>
</head>
<body>
<div class="canvas">
  <section class="card">
    <div class="card__band"></div>
    <div class="card__rule"></div>

    <div class="portrait" role="img" aria-label="Portrait photo of Marianne Collins"></div>

    <div class="brand">HARWELL<br>MORTGAGE ADVISORS</div>
    <div class="website">www.harwellmortgages.com</div>

    <div class="name name--first">MARIANNE</div>
    <div class="name name--last">COLLINS</div>

    <div class="phone">
      <svg class="phone__icon" viewBox="0 0 22 32" aria-hidden="true">
        <rect x="1.5" y="1.5" width="19" height="29" rx="3" fill="none" stroke="#ffffff" stroke-width="2.5"/>
        <line x1="1.5" y1="24" x2="20.5" y2="24" stroke="#ffffff" stroke-width="2"/>
        <circle cx="11" cy="27.3" r="1.3" fill="#ffffff"/>
      </svg>
      <span>415-555-0142</span>
    </div>

    <div class="title">
      <div class="title__role">VICE PRESIDENT</div>
      <div>MORTGAGE</div>
      <div>LENDING</div>
    </div>
  </section>
</div>
</body>
</html>
```